The Quiet Orchard of Copper Lanterns - 40-Week Tide Ledger

I am finishing a book that is designed to be super hands on. It steps he reader through a 90 day roadmap - as a pick up, put down action diary style piece. The foundational idea is to speak about the Quiet Orchard of Copper Lanterns. With a cost of living crisis this is designed to create action and understanding. I am looking for a cover for the ebook that will blow away the competitors in the category. I want it to be bright, attractive and leap off the lumora page - appeal to a wide audience. I have pasted in a file with the best selling books in the category so you can see what's working.

```html
<!DOCTYPE html>
<html lang="en">
<head>
<meta charset="utf-8">
<title>The Quiet Orchard of Copper Lanterns - 40-Week Tide Ledger</title>
<link rel="stylesheet" href="https://fonts.googleapis.com/css2?family=Anton&family=Oswald:wght@600&display=swap">
<style>
  :root {
    --ink: #111111;
    --sky-light: #eef6fb;
    --sky-mid: #bfe6f2;
    --aqua: #5fd6e4;
    --teal: #2fc7d0;
    --mint: #49d6b8;
    --land: rgba(255, 255, 255, 0.35);
  }
  * { margin: 0; padding: 0; box-sizing: border-box; }
  html, body { width: 849px; height: 1200px; overflow: hidden; background: #ffffff; }
  .cover {
    position: relative;
    width: 849px;
    height: 1200px;
    overflow: hidden;
  }
  .cover__backdrop {
    position: absolute;
    inset: 0;
    background:
      radial-gradient(ellipse 60% 45% at 20% 10%, var(--sky-light) 0%, transparent 70%),
      radial-gradient(ellipse 50% 40% at 25% 80%, var(--land) 0%, transparent 70%),
      linear-gradient(160deg, var(--sky-light) 0%, var(--sky-mid) 30%, var(--aqua) 62%, var(--teal) 82%, var(--mint) 100%);
  }
  .cover__rule {
    position: absolute;
    inset: 0;
  }
  .cover__title {
    position: absolute;
    inset: 0;
  }
  .title-word {
    font-family: "Anton", "Impact", sans-serif;
    fill: var(--ink);
  }
  .title-small {
    font-family: "Anton", "Impact", sans-serif;
    fill: var(--ink);
  }
  .subtitle {
    font-family: "Oswald", "Arial Narrow", sans-serif;
    font-weight: 600;
    fill: var(--ink);
    letter-spacing: 2px;
  }
</style>
</head>
<body>
  <main class="cover">
    <div class="cover__backdrop" role="img" aria-label="Soft world map in pale grey on a sky blue to aqua and mint gradient"></div>

    <svg class="cover__rule" width="849" height="1200" viewBox="0 0 849 1200" aria-hidden="true">
      <line x1="473" y1="0" x2="488" y2="1200" stroke="var(--ink)" stroke-width="2.5"/>
    </svg>

    <svg class="cover__title" width="849" height="1200" viewBox="0 0 849 1200">
      <text class="title-small" x="0" y="0" font-size="30" transform="translate(128 360) rotate(-90)">THE</text>
      <text class="title-word" x="140" y="355" font-size="125" textLength="555" lengthAdjust="spacingAndGlyphs">QUIET ORCHARD</text>
      <text class="title-small" x="705" y="325" font-size="52" textLength="58" lengthAdjust="spacingAndGlyphs">of</text>
      <text class="title-word" x="100" y="522" font-size="170" textLength="665" lengthAdjust="spacingAndGlyphs">COPPER</text>
      <text class="title-word" x="100" y="692" font-size="170" textLength="665" lengthAdjust="spacingAndGlyphs">LANTERNS</text>
      <text class="subtitle" x="150" y="742" font-size="40" textLength="560" lengthAdjust="spacingAndGlyphs">40-WEEK TIDE LEDGER</text>
    </svg>
  </main>
</body>
</html>
```